Velcrest-Aura

Letter heads, business cards, packaging envelopes big and small, and stationery
We have logo design and trademarked approval, we would lie to
upload design to help create this project.
This product was created for my Mother a 4 time diganosed Cancer
Survivor, This product has patent pending and now will be offered to the general public as well.
We are looking foward to working with all of you as this product
and stationary will be viewed worldwide.
Thanks
The Kindale Family

Target Market(s)

all ages and worldwide

Industry/Entity Type

Business

Requirements
Must have
• Our Logo

```html
<!DOCTYPE html>
<html lang="en">
<head>
<meta charset="utf-8">
<title>Velcrest-Aura Stationery</title>
<link href="https://fonts.googleapis.com/css2?family=Roboto+Condensed:wght@400;700;800&display=swap" rel="stylesheet">
<style>
:root{
  --red:#c00a0a;
  --navy:#0d3570;
  --paper:#ffffff;
  --backdrop:#2f2f2f;
  --frame:#8a8a8a;
}
*{box-sizing:border-box;margin:0;padding:0}
html,body{width:1200px;height:894px;overflow:hidden;background:var(--backdrop);font-family:"Roboto Condensed",Arial,sans-serif}
.canvas{position:relative;width:1200px;height:894px}

.brand{text-align:center;color:var(--navy);line-height:1}
.brand-name{font-weight:800;display:inline-flex;align-items:center;gap:6px;white-space:nowrap}
.brand-dot{display:inline-block;border-radius:50%;background:var(--red)}
.brand-tagline{font-weight:700;margin-top:2px;white-space:nowrap}
.label{color:var(--red)}

/* Letterhead */
.letterhead{position:absolute;left:60px;top:94px;width:480px;height:707px;background:var(--paper);overflow:hidden}
.letterhead .band-top{position:absolute;left:0;top:0;width:100%;height:16px;background:var(--red)}
.letterhead .band-top::after{content:"";position:absolute;right:0;top:0;width:120px;height:100%;background:var(--navy)}
.letterhead .brand{position:absolute;top:34px;left:0;right:0}
.letterhead .brand-name{font-size:28px}
.letterhead .brand-dot{width:18px;height:18px}
.letterhead .brand-tagline{font-size:12px}
.letterhead .footer-text{position:absolute;left:0;right:0;bottom:30px;text-align:center;font-size:8px;font-weight:700;color:var(--navy);white-space:nowrap}
.letterhead .band-bottom{position:absolute;left:0;bottom:0;width:100%;height:18px;background:var(--red)}
.letterhead .band-bottom::after{content:"";position:absolute;right:0;top:0;width:55%;height:100%;background:var(--navy)}

/* Envelope */
.envelope{position:absolute;left:590px;top:94px;width:550px;height:270px;background:var(--paper);overflow:hidden}
.envelope .flap{position:absolute;left:0;top:0}
.envelope .window{position:absolute;left:30px;top:150px;width:250px;height:80px;border:1px solid var(--frame);border-radius:16px}
.envelope .sender{position:absolute;right:24px;top:140px;width:220px}
.envelope .brand{text-align:left}
.envelope .brand-name{font-size:22px}
.envelope .brand-dot{width:14px;height:14px}
.envelope .brand-tagline{font-size:10px;padding-left:20px}
.envelope .sender-details{margin-top:8px;font-size:8px;font-weight:700;color:var(--navy);line-height:1.35;white-space:nowrap}
.envelope .band-bottom{position:absolute;left:0;bottom:0;width:100%;height:14px;background:var(--red)}
.envelope .band-bottom::after{content:"";position:absolute;right:0;top:0;width:42%;height:100%;background:var(--navy)}

/* Business cards */
.card{position:absolute;width:265px;height:165px;border-radius:18px;border:7px solid var(--navy);overflow:hidden}
.card-back{background:var(--red);display:flex;align-items:center;justify-content:center}
.card-back .brand-name{color:var(--paper);font-size:30px}
.card-back .brand-dot{width:20px;height:20px;background:var(--paper)}
.card-front{background:var(--paper);padding:16px 10px 0}
.card-front .brand-name{font-size:21px}
.card-front .brand-dot{width:13px;height:13px}
.card-front .brand-tagline{font-size:9px}
.holder{text-align:center;color:var(--red);margin-top:10px;line-height:1.1}
.holder-name{font-weight:800;font-size:14px}
.holder-role{font-weight:700;font-size:10px}
.card-details{margin-top:8px;text-align:center;font-size:7px;font-weight:700;color:var(--navy);line-height:1.45;white-space:nowrap}
.card-1{left:590px;top:420px}
.card-2{left:875px;top:420px}
.card-3{left:590px;top:620px}
.card-4{left:875px;top:620px}
</style>
</head>
<body>
<main class="canvas">

  <section class="letterhead">
    <div class="band-top"></div>
    <div class="brand">
      <div class="brand-name"><span class="brand-dot"></span>Velcrest-Aura</div>
      <div class="brand-tagline">Care Made Simple For Every Day</div>
    </div>
    <p class="footer-text">Lorem ipsum dolor sit amet, consectetuer adipiscing elit, sed diam nonummy nibh euismod tincidunt ut laoreet dolore <span class="label">P</span> 01234567 <span class="label">F</span> 01234567</p>
    <div class="band-bottom"></div>
  </section>

  <section class="envelope">
    <svg class="flap" width="550" height="120" viewBox="0 0 550 120" aria-hidden="true">
      <path d="M0 120 L0 95 L110 0 L550 0 L550 45 Z" fill="var(--red)"/>
    </svg>
    <div class="window"></div>
    <div class="sender">
      <div class="brand">
        <div class="brand-name"><span class="brand-dot"></span>Velcrest-Aura</div>
        <div class="brand-tagline">Care Made Simple For Every Day</div>
      </div>
      <p class="sender-details"><span class="label">ADDRESS</span> Lorem ipsum dolor sit amet, consectetuer<br>sed diam nonummy nibh euismod tincidunt<br><span class="label">P</span> 01234567 <span class="label">F</span> 01234567</p>
    </div>
    <div class="band-bottom"></div>
  </section>

  <article class="card card-back card-1">
    <div class="brand"><div class="brand-name"><span class="brand-dot"></span>Velcrest-Aura</div></div>
  </article>

  <article class="card card-front card-2">
    <div class="brand">
      <div class="brand-name"><span class="brand-dot"></span>Velcrest-Aura</div>
      <div class="brand-tagline">Care Made Simple For Every Day</div>
    </div>
    <div class="holder">
      <div class="holder-name">YOUR NAME HERE</div>
      <div class="holder-role">Occupation place</div>
    </div>
    <p class="card-details"><span class="label">ADDRESS</span> Lorem ipsum dolor sit amet, consectetuer adipiscing elit,<br>sed diam nonummy nibh euismod tincidunt ut laoreet dolore<br><span class="label">P</span> 01234567 <span class="label">F</span> 01234567</p>
  </article>

  <article class="card card-front card-3">
    <div class="brand">
      <div class="brand-name"><span class="brand-dot"></span>Velcrest-Aura</div>
      <div class="brand-tagline">Care Made Simple For Every Day</div>
    </div>
    <div class="holder">
      <div class="holder-name">YOUR NAME HERE</div>
      <div class="holder-role">Occupation place</div>
    </div>
    <p class="card-details"><span class="label">ADDRESS</span> Lorem ipsum dolor sit amet, consectetuer adipiscing elit,<br>sed diam nonummy nibh euismod tincidunt ut laoreet dolore<br><span class="label">P</span> 01234567 <span class="label">F</span> 01234567</p>
  </article>

  <article class="card card-back card-4">
    <div class="brand"><div class="brand-name"><span class="brand-dot"></span>Velcrest-Aura</div></div>
  </article>

</main>
</body>
</html>
```